The Verity (wine label)

We are creating a new wine label for our vineyard in Tasmania, Australia.
This wine is dedicated to a very special person and needs to reflect elegance, beauty and longevity. We are looking for a wine label that incorporates the artwork on the attached photo (serpent tattoo).
We are calling the wine "The Verity" and it is a Pinot Noir (red wine). It is a light bodied but elegant wine, which reflects the person that it is named after.
The wine will be a 2024 Vintage Pinot Noir.

```html
<!DOCTYPE html>
<html lang="en">
<head>
<meta charset="utf-8">
<title>The Verity – Pinot Noir Label</title>
<link rel="stylesheet" href="https://fonts.googleapis.com/css2?family=Cormorant+Garamond:wght@500&display=swap">
<style>
  :root {
    --backdrop: #2b2b2d;
    --label-black: #050505;
    --title-silver: #f1ecea;
    --type-light: #d9d6d4;
    --rainbow-red: #e8323c;
    --rainbow-orange: #f28a1e;
    --rainbow-yellow: #e6d22a;
    --rainbow-green: #5cc94a;
    --rainbow-blue: #3f7fe0;
    --rainbow-violet: #8d2ff0;
    --rainbow-magenta: #e02a8e;
  }
  * { margin: 0; padding: 0; box-sizing: border-box; }
  html, body {
    width: 1200px;
    height: 800px;
    overflow: hidden;
    background: var(--backdrop);
  }
  .canvas {
    position: relative;
    width: 1200px;
    height: 800px;
    display: flex;
    align-items: center;
    justify-content: center;
  }
  .wine-label {
    position: relative;
    width: 740px;
    height: 660px;
    background: var(--label-black);
    box-shadow: 0 20px 50px rgba(0,0,0,0.45);
  }
  .label-frame {
    position: absolute;
    inset: 0;
    width: 100%;
    height: 100%;
  }
  .serpent-artwork {
    position: absolute;
    left: 180px;
    top: 30px;
    width: 530px;
    height: 390px;
    border-radius: 48% 40% 46% 30% / 40% 38% 52% 46%;
    background:
      radial-gradient(ellipse at 85% 55%, rgba(224,42,142,0.55), transparent 55%),
      radial-gradient(ellipse at 55% 30%, rgba(92,201,74,0.45), transparent 55%),
      radial-gradient(ellipse at 35% 45%, rgba(242,138,30,0.5), transparent 55%),
      radial-gradient(ellipse at 10% 85%, rgba(232,50,60,0.5), transparent 50%),
      var(--label-black);
    opacity: 0.85;
  }
  .label-text {
    position: absolute;
    left: 0;
    right: 0;
    top: 440px;
    text-align: center;
    padding-left: 40px;
  }
  .wine-name {
    font-family: "Cormorant Garamond", serif;
    font-weight: 500;
    font-style: normal;
    font-size: 80px;
    line-height: 1;
    letter-spacing: 0.02em;
    color: var(--title-silver);
  }
  .wine-variety {
    margin-top: 22px;
    font-family: "Cormorant Garamond", serif;
    font-weight: 500;
    font-size: 30px;
    line-height: 1.1;
    letter-spacing: 0.12em;
    color: var(--type-light);
  }
  .wine-origin {
    margin-top: 8px;
    font-family: "Cormorant Garamond", serif;
    font-weight: 500;
    font-size: 17px;
    line-height: 1.2;
    letter-spacing: 0.06em;
    color: var(--type-light);
  }
</style>
</head>
<body>
<main class="canvas">
  <section class="wine-label">
    <svg class="label-frame" viewBox="0 0 740 660" aria-hidden="true">
      <defs>
        <linearGradient id="frame-rainbow" x1="0" y1="0" x2="1" y2="1">
          <stop offset="0" stop-color="#3f7fe0"/>
          <stop offset="0.3" stop-color="#5cc94a"/>
          <stop offset="0.45" stop-color="#e6d22a"/>
          <stop offset="0.6" stop-color="#f28a1e"/>
          <stop offset="0.75" stop-color="#e8323c"/>
          <stop offset="0.88" stop-color="#e02a8e"/>
          <stop offset="1" stop-color="#8d2ff0"/>
        </linearGradient>
      </defs>
      <rect x="22" y="22" width="696" height="616" fill="none" stroke="url(#frame-rainbow)" stroke-width="3"/>
    </svg>

    <div class="serpent-artwork" role="img" aria-label="Rainbow line-art serpent with scaled body winding across the label from a head at lower left to coils at upper right"></div>

    <div class="label-text">
      <h1 class="wine-name">The Verity</h1>
      <p class="wine-variety">PINOT NOIR</p>
      <p class="wine-origin">TASMANIA, AUSTRALIA / 2024</p>
    </div>
  </section>
</main>
</body>
</html>
```